Bright Ridge Electric Needs A Logo Design

We need a logo for my new company based out of Sacramento, Ca called Bright Ridge Electric. The name says it all, my electrical contracting business provides "Bright Ridge Professional Work" I'm open to any colors that pop and customers to say Wow. I would love to print my cards on metal.

Industry/Entity Type

Business

Contact Information for Business Card

The card needs to have as follows
Name of company: Bright Ridge Electric
My Name: Dorian Pelko
Phone # 916-382-5507
CL# 2087396
Email: brightridgeelectric@mailvance.net
and a slogan that represent "BRIGHT RIDGE"

Requirements
Must have
• The card needs to have as follows
• Name of company: Bright Ridge Electric
• My Name : Dorian Pelko
• Phone # 916-382-5507
• CL# 2087396
• Email: brightridgeelectric@mailvance.net
• and a slogan that represent "BRIGHT RIDGE"
Nice to have
• popping colors
• electrical Arcing

```html
<!DOCTYPE html>
<html lang="en">
<head>
<meta charset="utf-8">
<title>Bright Ridge Electric – Business Card</title>
<link rel="stylesheet" href="https://fonts.googleapis.com/css2?family=Ubuntu:wght@300;500;700&display=swap">
<style>
  :root {
    --backdrop: #e9e6e1;
    --card: #fbfbfb;
    --blue: #1877bf;
    --blue-light: #1f8fd6;
    --orange: #f0a023;
    --ink-blue: #2a86c8;
  }
  html, body {
    margin: 0;
    width: 1200px;
    height: 1022px;
    overflow: hidden;
    background: var(--backdrop);
    font-family: "Ubuntu", sans-serif;
  }
  .card {
    position: absolute;
    left: 150px;
    top: 254px;
    width: 900px;
    height: 514px;
    background: var(--card);
    box-shadow: 0 18px 40px rgba(60, 45, 30, 0.25);
    overflow: hidden;
  }
  .name-ribbon {
    position: absolute;
    right: 0;
    top: 70px;
    width: 410px;
    height: 72px;
    background: var(--blue);
    clip-path: polygon(38px 0, 100% 0, 100% 100%, 0 100%);
    display: flex;
    align-items: center;
    padding-left: 70px;
    box-sizing: border-box;
  }
  .name-ribbon h1 {
    margin: 0;
    color: #fff;
    font-weight: 500;
    font-size: 34px;
    letter-spacing: 2px;
    text-transform: uppercase;
  }
  .brand {
    position: absolute;
    left: 60px;
    top: 225px;
    display: flex;
    align-items: center;
    gap: 16px;
  }
  .brand-mark {
    width: 34px;
    height: 34px;
    background: var(--orange);
  }
  .brand-name {
    margin: 0;
    color: var(--blue);
    font-weight: 700;
    font-size: 30px;
    letter-spacing: 1px;
    text-transform: uppercase;
  }
  .contact {
    position: absolute;
    left: 330px;
    top: 352px;
    margin: 0;
    padding: 0;
    list-style: none;
  }
  .contact li {
    display: flex;
    align-items: center;
    gap: 12px;
    color: var(--ink-blue);
    font-weight: 300;
    font-size: 24px;
    line-height: 36px;
  }
  .contact svg {
    width: 16px;
    height: 16px;
    flex: none;
  }
  .band-blue {
    position: absolute;
    left: 0;
    bottom: 0;
    width: 540px;
    height: 40px;
    background: var(--blue);
  }
  .band-orange {
    position: absolute;
    right: 0;
    bottom: 0;
    width: 360px;
    height: 40px;
    background: var(--orange);
  }
</style>
</head>
<body>
  <section class="card">
    <div class="name-ribbon"><h1>Dorian Pelko</h1></div>

    <div class="brand">
      <span class="brand-mark"></span>
      <p class="brand-name">Bright Ridge Electric</p>
    </div>

    <ul class="contact">
      <li>
        <svg viewBox="0 0 16 16" aria-hidden="true"><rect x="2" y="2" width="12" height="12" rx="1.5" fill="none" stroke="#f0a023" stroke-width="1.6"/></svg>
        2087396
      </li>
      <li>
        <svg viewBox="0 0 16 16" aria-hidden="true"><path d="M4 2 L6.5 5 L5 6.8 Q6.5 9.8 9.2 11 L11 9.5 L14 12 L12.5 14 Q6 13.5 2 4 Z" fill="#f0a023"/></svg>
        916-382-5507
      </li>
      <li>
        <svg viewBox="0 0 16 16" aria-hidden="true"><rect x="1.5" y="3.5" width="13" height="9" fill="none" stroke="#f0a023" stroke-width="1.5"/><path d="M1.5 3.5 L8 9 L14.5 3.5" fill="none" stroke="#f0a023" stroke-width="1.5"/></svg>
        brightridgeelectric@mailvance.net
      </li>
    </ul>

    <div class="band-blue"></div>
    <div class="band-orange"></div>
  </section>
</body>
</html>
```